Brickline Rentals podcast postcard

I've launched a podcast about apartment investing, ownership and management which is newly up on orbix and wavlino. I want to create a postcard that I can mail to my client base to get them to subscribe

```html
<!DOCTYPE html>
<html lang="en">
<head>
<meta charset="utf-8">
<title>Brickline Rentals Podcast Postcard</title>
<link href="https://fonts.googleapis.com/css2?family=Montserrat:wght@600;800&family=Yellowtail&display=swap" rel="stylesheet">
<style>
  :root {
    --navy: #1f4b6e;
    --orange: #f08a38;
    --sky: #bfe2ee;
    --sky-deep: #9fcbdc;
    --pale: #e6eef6;
    --white: #ffffff;
    --stage: #d9dcdf;
    --line: #c9ced3;
  }
  * { box-sizing: border-box; margin: 0; padding: 0; }
  html, body { width: 1200px; height: 800px; overflow: hidden; }
  body {
    background: var(--stage);
    font-family: "Montserrat", Arial, sans-serif;
    position: relative;
  }
  .postcard {
    position: absolute;
    top: 210px;
    width: 540px;
    height: 360px;
    overflow: hidden;
    box-shadow: 0 6px 18px rgba(0,0,0,.18);
  }
  .postcard--back { left: 40px; background: var(--white); }
  .postcard--front { left: 620px; }

  /* Back */
  .back__panel {
    position: absolute; left: 0; top: 0; width: 270px; height: 360px;
    background: var(--pale);
  }
  .back__photo {
    position: absolute; left: 0; bottom: 0; width: 270px; height: 120px;
    background: linear-gradient(180deg, #dfe7ef 0%, #b9c9d8 60%, #9fb3c6 100%);
  }
  .brand-name {
    color: var(--navy);
    font-weight: 800;
    text-align: center;
    letter-spacing: .04em;
    text-transform: uppercase;
    line-height: 1.15;
  }
  .back__brand {
    position: absolute; left: 0; top: 70px; width: 270px; font-size: 24px;
  }
  .brand-sub {
    display: block; margin-top: 10px; font-size: .55em; letter-spacing: .35em;
  }
  .promo {
    position: absolute;
    background: var(--orange);
    color: var(--white);
    font-weight: 600;
    font-size: 12.5px;
    line-height: 1.3;
    text-align: center;
    padding: 16px 22px;
  }
  .promo--left {
    left: 70px; top: 240px; width: 230px; height: 92px;
    border-radius: 46px;
  }
  .promo--right {
    left: 270px; top: 86px; width: 150px; height: 120px;
    border-radius: 0 60px 60px 0;
    padding: 14px 12px;
  }
  .live-tag {
    display: inline-block; background: var(--white); color: var(--orange);
    font-size: 9px; font-weight: 800; padding: 0 5px; border-radius: 7px;
  }
  .platforms {
    display: flex; justify-content: center; gap: 14px; margin-top: 8px;
  }
  .platform { display: flex; align-items: center; gap: 4px; font-size: 12px; }
  .platform__dot {
    width: 10px; height: 10px; border-radius: 50%; background: var(--white);
  }
  .stamp-box {
    position: absolute; right: 26px; top: 22px; width: 62px; height: 72px;
    border: 1px solid var(--line);
  }

  /* Front */
  .front__photo {
    position: absolute; inset: 0;
    background: linear-gradient(100deg, var(--sky) 0%, var(--sky) 55%, var(--sky-deep) 80%, #e8f3f7 100%);
  }
  .front__brand {
    position: absolute; left: 90px; top: 90px; width: 300px; font-size: 34px;
  }
  .ribbon {
    position: absolute; left: 60px; top: 270px; width: 440px; height: 42px;
    transform: rotate(-11deg);
  }
  .ribbon__text {
    position: absolute; inset: 0;
    display: flex; align-items: center; justify-content: center;
    font-family: "Yellowtail", cursive;
    font-size: 24px; color: var(--white);
  }
</style>
</head>
<body>
  <section class="postcard postcard--back" aria-label="Postcard back">
    <div class="back__panel"></div>
    <div class="back__photo" role="img" aria-label="Photo of an apartment tower seen from below"></div>
    <div class="brand-name back__brand">Brickline Rentals<span class="brand-sub">Podcast</span></div>
    <div class="promo promo--left">
      “Brickline Rentals” Podcast<br>is <span class="live-tag">LIVE</span> Subscribe on:
      <div class="platforms">
        <span class="platform"><span class="platform__dot"></span>orbix</span>
        <span class="platform"><span class="platform__dot"></span>wavlino</span>
      </div>
    </div>
    <div class="promo promo--right">
      “Brickline Rentals” Podcast is <span class="live-tag">LIVE</span> Subscribe on:
      <div class="platforms">
        <span class="platform"><span class="platform__dot"></span>orbix</span>
        <span class="platform"><span class="platform__dot"></span>wavlino</span>
      </div>
    </div>
    <div class="stamp-box"></div>
  </section>

  <section class="postcard postcard--front" aria-label="Postcard front">
    <div class="front__photo" role="img" aria-label="Pale blue photo of apartment buildings against the sky"></div>
    <div class="brand-name front__brand">Brickline Rentals<span class="brand-sub">Podcast</span></div>
    <div class="ribbon">
      <svg width="440" height="42" viewBox="0 0 440 42" aria-hidden="true">
        <polygon points="0,0 440,0 424,21 440,42 0,42 16,21" fill="#f08a38"/>
      </svg>
      <span class="ribbon__text">Investing, Ownership &amp; Management</span>
    </div>
  </section>
</body>
</html>
```